Satchel & Compass needs new business card design

I need a new business card design. I'm looking for out-of-the-box design which represents the freedom of being a location independent entrepreneur.
I offer coaching, retreats and trips.
I would like to see designs with and without the photo.
Colors I use are black (#000000), green (#25A796) and brown (#D7C38C)
Website satchelandcompass.com

Target Market(s)

location independent entrepreneurs, digital nomads, people looking to swap the 9 to 5 for a lifestyle business

Industry/Entity Type

Business

Contact Information for Business Card

Petra Varga
Your Lifestyle Business Coach, Retreat & Trip Leader
http://satchelandcompass.com
hello@satchelandcompass.com
Live a life you don't need a holiday from

Font styles to use
Serif
Sans Serif

Requirements
Must have
• One side should contain only the logo. I would also consider having the "Live a life you don't need a holiday from" on that side too (depending on how it looks)
• Please show both sides on the designs.

```html
<!DOCTYPE html>
<html lang="en">
<head>
<meta charset="utf-8">
<title>Satchel &amp; Compass — Business Card</title>
<link rel="stylesheet" href="https://fonts.googleapis.com/css2?family=Roboto+Condensed:wght@400;700&family=Montserrat:wght@400;600;700&display=swap">
<style>
  :root {
    --backdrop: #2b2b2d;
    --paper: #ffffff;
    --paper-shade: #f1f3f4;
    --aqua: #1cb6d6;
    --aqua-deep: #0fa3c6;
    --aqua-pale: #bfe9f3;
    --ink: #111111;
    --muted: #9a9ea3;
  }
  * { box-sizing: border-box; margin: 0; padding: 0; }
  html, body {
    width: 1200px; height: 900px; overflow: hidden;
    background: var(--backdrop);
  }
  .canvas { position: relative; width: 1200px; height: 900px; }

  .card {
    position: absolute;
    width: 640px; height: 366px;
    background: var(--paper);
    overflow: hidden;
    box-shadow: 0 14px 30px rgba(0,0,0,.45);
  }
  .card--front { left: 110px; top: 60px; }
  .card--back  { left: 450px; top: 470px; }

  /* Front */
  .front-pattern { position: absolute; left: 0; top: 0; width: 640px; height: 366px; }
  .logo {
    position: absolute; left: 34px; top: 150px;
    font-family: "Montserrat", sans-serif;
    font-weight: 700; font-size: 30px; letter-spacing: 1px;
    color: var(--ink); text-transform: uppercase;
  }

  /* Back */
  .back-band {
    position: absolute; left: 0; top: 0; width: 640px; height: 205px;
    background: linear-gradient(180deg, var(--aqua) 0%, var(--aqua-deep) 100%);
  }
  .back-pattern { position: absolute; left: 0; top: 0; width: 640px; height: 205px; }
  .identity {
    position: absolute; right: 30px; top: 96px; text-align: right; color: var(--paper);
  }
  .identity__name {
    font-family: "Roboto Condensed", sans-serif; font-weight: 700; font-size: 40px; line-height: 1;
  }
  .identity__role {
    font-family: "Roboto Condensed", sans-serif; font-weight: 400; font-size: 10.5px; margin-top: 4px;
  }
  .contacts {
    position: absolute; left: 0; top: 222px; width: 640px;
    font-family: "Montserrat", sans-serif; font-size: 13px; color: var(--muted);
  }
  .contact-row {
    display: flex; justify-content: center; align-items: center; gap: 8px; height: 34px;
  }
  .contact-row .divider { width: 1px; height: 18px; background: var(--muted); margin: 0 16px; }
  .contact-item { display: flex; align-items: center; gap: 8px; }
  .icon { width: 14px; height: 14px; fill: var(--muted); }
</style>
</head>
<body>
<main class="canvas">

  <section class="card card--front" aria-label="Card front">
    <svg class="front-pattern" viewBox="0 0 640 366" role="img" aria-label="Geometric pattern of striped and dotted triangles in pale blue">
      <defs>
        <linearGradient id="frontTone" x1="0" y1="0" x2="1" y2="1">
          <stop offset="0" stop-color="#d6f1f8"/>
          <stop offset="1" stop-color="#9fdcee"/>
        </linearGradient>
      </defs>
      <polygon points="300,0 640,0 640,230 420,366 330,366 300,170" fill="url(#frontTone)" opacity=".75"/>
    </svg>
    <div class="logo">Satchel &amp; Compass</div>
  </section>

  <section class="card card--back" aria-label="Card back">
    <div class="back-band"></div>
    <svg class="back-pattern" viewBox="0 0 640 205" role="img" aria-label="Geometric pattern of striped white triangles on blue">
      <defs>
        <linearGradient id="backTone" x1="0" y1="0" x2="1" y2="0">
          <stop offset="0" stop-color="#7fd6ea"/>
          <stop offset="1" stop-color="#3cc2df"/>
        </linearGradient>
      </defs>
      <polygon points="0,60 250,0 330,205 0,205" fill="url(#backTone)" opacity=".6"/>
    </svg>
    <div class="identity">
      <div class="identity__name">Petra Varga</div>
      <div class="identity__role">Your Lifestyle Business Coach, Retreat &amp; Trip Leader</div>
    </div>

    <div class="contacts">
      <div class="contact-row">
        <span class="contact-item">
          <svg class="icon" viewBox="0 0 24 24"><path d="M6.6 10.8a15.1 15.1 0 0 0 6.6 6.6l2.2-2.2a1 1 0 0 1 1-.25 11.4 11.4 0 0 0 3.6.57 1 1 0 0 1 1 1V20a1 1 0 0 1-1 1A17 17 0 0 1 3 4a1 1 0 0 1 1-1h3.5a1 1 0 0 1 1 1c0 1.25.2 2.45.57 3.57a1 1 0 0 1-.25 1z"/></svg>
          +00 123 456 789
        </span>
      </div>
      <div class="contact-row">
        <span class="contact-item">
          <svg class="icon" viewBox="0 0 24 24"><path d="M12 2a7 7 0 0 0-7 7c0 5.25 7 13 7 13s7-7.75 7-13a7 7 0 0 0-7-7zm0 9.5A2.5 2.5 0 1 1 12 6.5a2.5 2.5 0 0 1 0 5z"/></svg>
          123 eiusmod incididunt ut labore 12345
        </span>
        <span class="divider"></span>
        <span class="contact-item">
          <svg class="icon" viewBox="0 0 24 24"><path d="M5 2l14 11-6.2.8 3.6 7.2-2.6 1.2-3.5-7.3L5 19z"/></svg>
          satchelandcompass.com
        </span>
      </div>
      <div class="contact-row">
        <span class="contact-item">
          <svg class="icon" viewBox="0 0 24 24"><path d="M3 5h18a1 1 0 0 1 1 1v12a1 1 0 0 1-1 1H3a1 1 0 0 1-1-1V6a1 1 0 0 1 1-1zm9 7.5L20 7H4z"/></svg>
          hello@satchelandcompass.com
        </span>
      </div>
    </div>
  </section>

</main>
</body>
</html>
```